New Lead input page design

Attached is our concept of a new lead input screen for the back-end of our website which is a tool for a loan agent (2 page PDF attached)

1. This is the first of many other data input screen projects for our website, so the designer that ends up with us will have quite a bit of add on new projects.

2. HERE IS THE LINK WITH THE SAMPLE OF ALL THE CURRENT CONTROLS:
http://apps.brimtally88.net/controlWidgets.html

3. The colors and hues of: either GREEN & GREYS or BLUE & GREYS.

4. I think some gradients and shadows adds depth and sophistication. Basically trying to get away from old school flat, one dimensional data screen inputs and add some design flare to it.

5. Upon completion we will need the HTML of the design etc and we will code the input fields directly.

6. See attached files for the entire input screen. Please also add the data input space (see sample) to your design.

Thank you

Reason: We are extending the deadline to give us time to ask current designs to complete slight revisions

Reason: Finalizing the selection for one last variation detailed to current designers

```html
<!DOCTYPE html>
<html lang="en">
<head>
<meta charset="utf-8">
<title>Lead Input</title>
<link href="https://fonts.googleapis.com/css2?family=Open+Sans:wght@400;600&family=Varela+Round&display=swap" rel="stylesheet">
<style>
:root{
  --head-top:#5ec4f3;
  --head-bot:#2f93e3;
  --line:#e3e6ea;
  --label:#3d4248;
  --value:#1f2327;
  --row-fade:#f3f4f6;
  --light-top:#a5e6fc;
  --light-bot:#3cc0f3;
  --dark-top:#40a9f2;
  --dark-bot:#1b66d6;
  --foot:#e8e9eb;
}
*{box-sizing:border-box;margin:0;padding:0}
html,body{width:818px;height:1200px;overflow:hidden;background:#fff}
body{font-family:"Open Sans",Arial,sans-serif;position:relative}
.topbar{height:75px;background:linear-gradient(180deg,var(--head-top),var(--head-bot));display:flex;align-items:center;position:relative;color:#fff}
.lead-category{position:absolute;left:70px;top:24px;font-family:"Varela Round","Open Sans",sans-serif;font-size:19px;display:flex;align-items:center;gap:7px}
.nav-item{position:absolute;top:0;height:75px;display:flex;flex-direction:column;align-items:center;justify-content:center;gap:5px;font-family:"Varela Round","Open Sans",sans-serif;font-size:12px;transform:translateX(-50%)}
.nav-sep{position:absolute;top:0;width:1px;height:75px;background:rgba(255,255,255,.25)}
.row{position:relative;border-bottom:1px solid var(--line);background:linear-gradient(180deg,#fff 55%,var(--row-fade));display:flex}
.badge-cell{width:200px;border-right:1px solid var(--line);display:flex;align-items:center;justify-content:center}
.badge{width:80px;height:80px;border-radius:50%;display:flex;align-items:center;justify-content:center;text-align:center;color:#fff;font-family:"Varela Round","Open Sans",sans-serif;font-size:15px;line-height:17px;box-shadow:0 0 0 3px #fff,0 1px 5px 3px rgba(0,0,0,.12)}
.badge.light{background:linear-gradient(180deg,var(--light-top),var(--light-bot));color:#12426a}
.badge.dark{background:linear-gradient(180deg,var(--dark-top),var(--dark-bot))}
.badge.small{font-size:12.5px;line-height:16px}
.cell{display:grid;grid-template-columns:98px 1fr;grid-auto-rows:min-content;align-content:start;font-size:10.3px;line-height:20.5px}
.cell.mid{width:266px;border-right:1px solid var(--line);padding-left:40px}
.cell.side{flex:1;padding-left:43px;grid-template-columns:123px 1fr}
.cell dt{color:var(--label)}
.cell dd{color:var(--value);font-weight:600}
.footer{position:absolute;left:0;top:1148px;width:818px;height:52px;background:var(--foot);font-size:8.6px;color:#3a3e42}
.footer .legal{position:absolute;left:58px;top:18px}
.footer .page{position:absolute;right:12px;top:33px;font-size:9.5px}
</style>
</head>
<body>
<header class="topbar">
  <div class="lead-category">Lead Category
    <svg width="18" height="18" viewBox="0 0 18 18" fill="none" stroke="#fff" stroke-width="1.8"><circle cx="9" cy="9" r="7.5"/><path d="M9 4.5v8M5.8 9.5 9 12.7l3.2-3.2"/></svg>
  </div>
  <div class="nav-sep" style="left:374px"></div>
  <div class="nav-sep" style="left:474px"></div>
  <div class="nav-sep" style="left:551px"></div>
  <div class="nav-sep" style="left:658px"></div>
  <div class="nav-item" style="left:320px">
    <svg width="28" height="22" viewBox="0 0 28 22" fill="none" stroke="#fff" stroke-width="1.6"><rect x="4" y="2" width="20" height="14" rx="1"/><path d="M1 19h26"/></svg>Sticky Note</div>
  <div class="nav-item" style="left:425px">
    <svg width="30" height="22" viewBox="0 0 30 22"><rect x="2" y="3" width="24" height="16" rx="3" fill="#fff"/><circle cx="14" cy="11" r="4.5" fill="var(--head-bot)"/><circle cx="26" cy="17" r="3.5" fill="#fff" stroke="var(--head-bot)" stroke-width="1.2"/></svg>Snap Shot</div>
  <div class="nav-item" style="left:514px">
    <svg width="22" height="26" viewBox="0 0 22 26" fill="none" stroke="#fff" stroke-width="1.6"><path d="M11 2c1 5 8 8 8 15a8 8 0 0 1-16 0c0-4 3-6 4-9 1 3 2 4 4 5 0-4-1-8 0-11z"/></svg>Alerts</div>
  <div class="nav-item" style="left:606px">
    <svg width="22" height="24" viewBox="0 0 22 24" fill="none" stroke="#fff" stroke-width="1.6"><rect x="2" y="2" width="18" height="20"/><path d="M6 8h10M6 12h10M6 16h10"/></svg>Lead Notes</div>
  <div class="nav-item" style="left:707px">
    <svg width="24" height="24" viewBox="0 0 24 24" fill="none" stroke="#fff" stroke-width="1.6"><rect x="2" y="4" width="20" height="18" rx="1"/><path d="M7 1v5M17 1v5M2 9h20"/><g fill="#fff" stroke="none"><rect x="5" y="12" width="2.5" height="2.5"/><rect x="10.7" y="12" width="2.5" height="2.5"/><rect x="16.5" y="12" width="2.5" height="2.5"/><rect x="5" y="17" width="2.5" height="2.5"/><rect x="10.7" y="17" width="2.5" height="2.5"/><rect x="16.5" y="17" width="2.5" height="2.5"/></g></svg>Calendar</div>
</header>

<section class="row" style="height:131px">
  <div class="badge-cell"><div class="badge light">Clients</div></div>
  <dl class="cell mid" style="padding-top:24px"><dt>Brrower:</dt><dd>Daniel Horvat</dd><dt>Application:</dt><dd>Joint</dd><dt>Lead Stat:</dt><dd>03</dd><dt>Demo Stat:</dt><dd>04</dd></dl>
  <dl class="cell side" style="padding-top:24px"><dt>Co-Brrower:</dt><dd>Elena Horvat</dd><dt>Relationship:</dt><dd>Husband &amp; Wife</dd><dt>Add Borrowers:</dt><dd>N/A</dd></dl>
</section>

<section class="row" style="height:128px">
  <div class="badge-cell"><div class="badge dark">Existing<br>Loan</div></div>
  <dl class="cell mid" style="padding-top:21px"><dt>Current Amount:</dt><dd>$335,758</dd><dt>Current Loan:</dt><dd>30 year fix – 5.5%</dd><dt>Apprx. Last Refi:</dt><dd>4 years ago</dd><dt>Add more Loans</dt><dd>$59,000 - Heloc</dd></dl>
  <dl class="cell side" style="padding-top:21px"><dt>How many loans:</dt><dd>2 Pay off both? Yes</dd><dt>Current P &amp; I:</dt><dd>$2,200</dd><dt>Tax &amp; Insurance:</dt><dd>$500</dd><dt>Total Payment:</dt><dd>$2,650</dd></dl>
</section>

<section class="row" style="height:138px">
  <div class="badge-cell"><div class="badge light small" style="margin-left:6px">New<br>Loan</div></div>
  <dl class="cell mid" style="padding-top:32px;padding-left:44px"><dt>New Amount:</dt><dd>$335,758</dd><dt>New Loan:</dt><dd>30 year fix - “select”</dd><dt>Quoted Rate:</dt><dd>5%</dd></dl>
  <dl class="cell side" style="padding-top:32px"><dt>New Loan Purpose:</dt><dd>Rate &amp; Term</dd><dt>Closing Costs:</dt><dd>$4500</dd><dt>Lender Credit:</dt><dd>$450</dd></dl>
</section>

<section class="row" style="height:142px">
  <div class="badge-cell"><div class="badge dark">Contact</div></div>
  <dl class="cell mid" style="padding-top:33px"><dt>Main Phone:</dt><dd>111-111-1111</dd><dt>Email:</dt><dd>Daniel@quillmail.com</dd><dt>Address:</dt><dd style="line-height:17px;padding-top:2px">418 Orbit court<br>San Diego CA 92265</dd></dl>
  <dl class="cell side" style="padding-top:33px"><dt>Main Phone:</dt><dd>111-111-1111</dd><dt>Email:</dt><dd>Elena@quillmail.com</dd><dt>Address:</dt><dd style="line-height:17px;padding-top:2px">418 Orbit court<br>San Diego CA 92265</dd></dl>
</section>

<section class="row" style="height:142px">
  <div class="badge-cell"><div class="badge light">Credit</div></div>
  <dl class="cell mid" style="padding-top:21px"><dt>DOB:</dt><dd>02/22/1975</dd><dt>Daniel’s Social:</dt><dd>123-45-6789</dd><dt>Credit Score:</dt><dd>700 688 744</dd><dt>Credit Pull Date:</dt><dd>04/28/14</dd><dt>DTI:</dt><dd>44% - 32%</dd></dl>
  <dl class="cell side" style="padding-top:21px"><dt>DOB:</dt><dd>01/25/1973</dd><dt>Elena’s Social:</dt><dd>123-45-6789</dd><dt>Credit Score:</dt><dd>700 688 744</dd><dt>Credit Age:</dt><dd>04/28/14</dd><dt>Credit Impression:</dt><dd>Excellent</dd></dl>
</section>

<section class="row" style="height:154px">
  <div class="badge-cell"><div class="badge light">Property</div></div>
  <dl class="cell mid" style="padding-top:32px"><dt>Address::</dt><dd style="line-height:15px;padding-top:3px;padding-bottom:5px">418 Orbit court<br>San Diego CA 92265</dd><dt>Property Type:</dt><dd>SFR</dd><dt>Residency:</dt><dd>Primary</dd><dt>Year Built:</dt><dd>1981</dd></dl>
  <dl class="cell side" style="padding-top:32px"><dt>Subject Property:</dt><dd>Yes - 1 of 3</dd><dt>Number of Properties:</dt><dd>3 - Add More</dd><dt>Special Upgrades:</dt><dd>Added a room &amp; roof</dd><dt>Approximate Value:</dt><dd>$445,000</dd><dt>Appraised Value:</dt><dd>$405,000</dd></dl>
</section>

<section class="row" style="height:238px;border-bottom:none">
  <div class="badge-cell"><div class="badge dark" style="margin-right:6px">Property</div></div>
  <dl class="cell mid" style="padding-top:41px;padding-left:30px"><dt>Income Source:</dt><dd>Ferncrest Labs</dd><dt>Address:</dt><dd>207 Marlow way</dd><dt>Work phone:</dt><dd>555-555-555</dd><dt>Position:</dt><dd>Admin</dd><dt>Length:</dt><dd>2 years</dd><dt>Term:</dt><dd>$3,000</dd><dt>Income:</dt><dd>$3,000</dd><dt>Other Income:</dt><dd>$ 1,500</dd></dl>
  <dl class="cell side" style="padding-top:41px;padding-left:45px"><dt>Income Source:</dt><dd>Ferncrest Labs</dd><dt>Address:</dt><dd>207 Marlow way</dd><dt>Work phone:</dt><dd>555-555-555</dd><dt>Position:</dt><dd>Manager</dd><dt>Length:</dt><dd>4 years</dd><dt>Term:</dt><dd>2 years</dd><dt>Income:</dt><dd>$4,500</dd><dt>Other Income:</dt><dd>$1,950</dd></dl>
</section>

<footer class="footer">
  <p class="legal">© 2014 Company Name.&nbsp; All right reserved.&nbsp; Term of Use</p>
  <p class="page">X14</p>
</footer>
</body>
</html>
```